Technological Event Invitation

We need a invitation design for a technological event we are hosting along with our partner. The target of this event are Vice president, Managers and CEO of the most important companies (bank, insurrance companies, other) in the dominican republic.

It is a flat invitation and the size is 5” x 7”.

Title: API Management
"Transforma tu negocio con API Management a través de la estrategia de digitalización"
Date: Jueves 10 de Marzo del 2016
Time: 9:00 am - 5 pm.
Place: Resturant Casa Rivolta C/ Marcos Ibarra Lugo esq. Tomás Revel.
Host: Novaldo, SRL & KV Systems
RSVP: 809 555 47 13

The final design should have two logo one being Novaldo ( the company hosting the event) and KV logo ( partner). Please consider that the desgin should represent tecnhology world.

Target Market(s)

Financial Institutions,Corporations, Goverment Institution

Industry/Entity Type

Event

Requirements
Must have
• 1. Kv logo
• 2. novaldo Logo
• 3. The invitation should show that the is a tecnological event on APIM.
Nice to have
• our colors integrated on the invitations

```html
<!DOCTYPE html>
<html lang="es">
<head>
<meta charset="utf-8">
<title>API Management – Invitación</title>
<link rel="stylesheet" href="https://fonts.googleapis.com/css2?family=Montserrat:wght@500;700;800&family=Roboto+Condensed:wght@400&family=Open+Sans:wght@400;700&display=swap">
<style>
  :root {
    --navy: #1f3d6e;
    --navy-dark: #17305a;
    --red: #d6312f;
    --ink: #2b2b2b;
    --paper: #f4f5f7;
    --white: #ffffff;
    --partner: #0b6fb3;
  }
  * { margin: 0; padding: 0; box-sizing: border-box; }
  html, body { width: 857px; height: 1200px; overflow: hidden; background: var(--paper); }
  .invitation {
    position: relative; width: 857px; height: 1200px;
    background: radial-gradient(ellipse at 50% 40%, var(--white) 0%, var(--paper) 75%);
    font-family: "Open Sans", sans-serif; color: var(--ink);
  }
  .host-brand {
    position: absolute; left: 40px; top: 40px;
    display: flex; align-items: center; gap: 14px;
  }
  .host-brand .dot { width: 54px; height: 54px; border-radius: 50%; background: var(--red); }
  .host-brand .name {
    font-family: "Montserrat", sans-serif; font-weight: 800;
    font-size: 44px; letter-spacing: 1px; color: var(--navy-dark); line-height: 1;
  }
  .host-brand .tagline {
    font-family: "Montserrat", sans-serif; font-weight: 700;
    font-size: 15px; letter-spacing: 0.5px; color: var(--navy-dark); margin-top: 4px;
  }
  .partner-brand {
    position: absolute; right: 48px; top: 44px;
    font-family: "Montserrat", sans-serif; font-weight: 800;
    font-size: 64px; color: var(--partner); line-height: 1;
  }
  .title {
    position: absolute; left: 0; right: 0; top: 252px; text-align: center;
    font-family: "Montserrat", sans-serif; color: var(--navy);
  }
  .title .main { font-weight: 800; font-size: 104px; line-height: 1; }
  .title .sub { font-weight: 700; font-size: 32px; letter-spacing: 1px; margin-top: 8px; }
  .quote-box {
    position: absolute; left: 178px; top: 432px; width: 530px; height: 388px;
    background: var(--navy);
  }
  .quote-box .mark {
    position: absolute; font-family: "Montserrat", sans-serif; font-weight: 800;
    font-size: 190px; line-height: 1; color: var(--navy);
  }
  .quote-box .mark.open { left: -58px; top: -40px; }
  .quote-box .mark.close { right: -56px; bottom: -150px; }
  .quote-box .text {
    position: absolute; left: 46px; top: 38px; right: 30px;
    border-left: 4px solid var(--white); padding-left: 16px;
    font-family: "Roboto Condensed", sans-serif; font-size: 47px; line-height: 1.2;
    color: var(--white);
  }
  .details {
    position: absolute; left: 24px; right: 24px; top: 1010px;
    display: grid; grid-template-columns: 400px 1fr; row-gap: 14px; column-gap: 20px;
    font-size: 17px; color: var(--ink);
  }
  .detail { display: flex; align-items: center; gap: 10px; }
  .detail svg { width: 30px; height: 30px; flex: none; }
  .detail b { font-weight: 700; }
</style>
</head>
<body>
<main class="invitation">
  <header>
    <div class="host-brand">
      <span class="dot"></span>
      <div>
        <div class="name">NOVALDO</div>
        <div class="tagline">IT CONSULTING AND SERVICES</div>
      </div>
    </div>
    <div class="partner-brand">KV</div>
  </header>

  <h1 class="title">
    <div class="main">API</div>
    <div class="sub">MANAGEMENT</div>
  </h1>

  <section class="quote-box">
    <span class="mark open">“</span>
    <p class="text">Transforma tu negocio con API Management a través de la estrategia de digitalización</p>
    <span class="mark close">”</span>
  </section>

  <section class="details">
    <div class="detail">
      <svg viewBox="0 0 30 30"><circle cx="15" cy="15" r="15" fill="#1f3d6e"/><rect x="8" y="9" width="14" height="13" rx="1.5" fill="none" stroke="#fff" stroke-width="2"/><line x1="8" y1="13" x2="22" y2="13" stroke="#fff" stroke-width="2"/></svg>
      <span><b>Date:</b> Jueves 10 de Marzo del 2016</span>
    </div>
    <div class="detail">
      <svg viewBox="0 0 30 30"><circle cx="15" cy="15" r="15" fill="#1f3d6e"/><path d="M15 7c-3.3 0-6 2.6-6 5.9C9 17.5 15 23 15 23s6-5.5 6-10.1C21 9.6 18.3 7 15 7z" fill="#fff"/><circle cx="15" cy="13" r="2.2" fill="#1f3d6e"/></svg>
      <span>C/ Marcos Ibarra Lugo esq. Tomás Revel.</span>
    </div>
    <div class="detail">
      <svg viewBox="0 0 30 30"><circle cx="15" cy="15" r="15" fill="#1f3d6e"/><circle cx="15" cy="15" r="7.5" fill="none" stroke="#fff" stroke-width="2"/><path d="M15 10.5V15l3 2" fill="none" stroke="#fff" stroke-width="2"/></svg>
      <span><b>Time:</b> 9:00 am - 5 pm.</span>
    </div>
    <div class="detail">
      <svg viewBox="0 0 30 30"><circle cx="15" cy="15" r="15" fill="#1f3d6e"/><circle cx="15" cy="11.5" r="3.5" fill="#fff"/><path d="M8.5 22c0-3.8 2.9-6 6.5-6s6.5 2.2 6.5 6z" fill="#fff"/></svg>
      <span><b>Host:</b> Novaldo, SRL &amp; KV Systems</span>
    </div>
    <div class="detail">
      <svg viewBox="0 0 30 30"><circle cx="15" cy="15" r="15" fill="#1f3d6e"/><path d="M15 7c-3.3 0-6 2.6-6 5.9C9 17.5 15 23 15 23s6-5.5 6-10.1C21 9.6 18.3 7 15 7z" fill="#fff"/><circle cx="15" cy="13" r="2.2" fill="#1f3d6e"/></svg>
      <span><b>Place:</b> Resturant Casa Rivolta</span>
    </div>
    <div class="detail">
      <svg viewBox="0 0 30 30"><circle cx="15" cy="15" r="15" fill="#1f3d6e"/><path d="M11 8.5l2.5-.5 1.5 4-2 1.3c.8 1.8 2 3 3.7 3.8l1.3-2 4 1.5-.5 2.5c-.3 1.2-1.5 1.8-2.7 1.5C13.5 19.5 10.5 16.5 9.4 11.3c-.3-1.2.4-2.5 1.6-2.8z" fill="#fff"/></svg>
      <span><b>RSVP:</b> 809 555 47 13</span>
    </div>
  </section>
</main>
</body>
</html>
```